Cedarline Residences —-

Letter head for my apartment building of 15 Floors
In Kampala, Uganda

CEDARLINE RESIDENCIES
14 KIVARA RIDGE ROAD
NAGURU - KAMPALA
P.O. BOX 38516
KAMPALA— UGANDA

```html
<!DOCTYPE html>
<html lang="en">
<head>
<meta charset="utf-8">
<title>Cedarline Residences — Letterhead</title>
<link rel="stylesheet" href="https://fonts.googleapis.com/css2?family=Saira+Semi+Condensed:wght@700&family=PT+Sans:wght@400&display=swap">
<style>
  :root {
    --backdrop: #e1e1e1;
    --paper: #ffffff;
    --brand-blue: #0b6293;
    --ink-dark: #231f20;
    --ink-text: #3a3a3a;
    --rule: #8a8a8a;
  }
  * { box-sizing: border-box; margin: 0; padding: 0; }
  html, body {
    width: 1200px;
    height: 997px;
    overflow: hidden;
    background: var(--backdrop);
  }
  .canvas {
    position: relative;
    width: 1200px;
    height: 997px;
  }
  .letterhead {
    position: absolute;
    left: 300px;
    top: 74px;
    width: 600px;
    height: 848px;
    background: var(--paper);
    box-shadow: 0 6px 18px rgba(0,0,0,0.18);
    overflow: hidden;
  }
  .masthead {
    position: absolute;
    left: 58px;
    top: 62px;
    display: inline-flex;
    flex-direction: column;
    align-items: flex-end;
  }
  .masthead__name {
    font-family: "Saira Semi Condensed", sans-serif;
    font-weight: 700;
    font-size: 21px;
    letter-spacing: 0.8px;
    line-height: 1;
    color: var(--brand-blue);
  }
  .masthead__rule {
    width: 82%;
    height: 1px;
    background: var(--rule);
    margin: 7px 0 5px;
  }
  .masthead__address {
    font-family: "PT Sans", sans-serif;
    font-size: 11.5px;
    line-height: 1.3;
    color: var(--ink-text);
    text-align: right;
  }
  .footer-bars {
    position: absolute;
    right: 0;
    bottom: 0;
  }
</style>
</head>
<body>
  <div class="canvas">
    <div class="letterhead">
      <header class="masthead">
        <div class="masthead__name">CEDARLINE RESIDENCIES</div>
        <div class="masthead__rule"></div>
        <address class="masthead__address" style="font-style:normal">
          14 Kivara Ridge Road, Naguru - Kampala<br>
          P.O. Box 38516, Kampala— Uganda
        </address>
      </header>

      <svg class="footer-bars" width="310" height="36" viewBox="0 0 310 36" aria-hidden="true">
        <path d="M0 36 V14 A14 14 0 0 1 14 0 H226 V36 Z" fill="var(--ink-dark)"/>
        <rect x="229" y="0" width="81" height="36" fill="var(--brand-blue)"/>
      </svg>
    </div>
  </div>
</body>
</html>
```